Wine Label: Corvinte

The project is to create 3 wine labels. The brand name is "Corvinte"

What we need is to have 3 versions: red wine, white wine and rose.

The wine is for young and modern people, between 21 and 31 years old, so it need to be casual, modern and fun, but at the same time it needs to keep the Premiums of a good European wine.

It is from Italy.

Target Market(s)

Young adults, between 21 and 31 years old. wine lovers

Requirements
Must have
• - Modern colors (Black, silver, red, etc.)
• - Clean label
• - Clear font
• - Style
• - The brand + the type of wine (red, white or rose)
Nice to have
• - A symbol to represent the brand
Should not have
• - Many elements
• - No clear fonts
• - No funny colors

```html
<!DOCTYPE html>
<html lang="en">
<head>
<meta charset="utf-8">
<title>Corvinte White – Wine Label</title>
<link rel="stylesheet" href="https://fonts.googleapis.com/css2?family=Oleo+Script:wght@700&family=Arimo:wght@400&display=swap">
<style>
  :root {
    --page: #ffffff;
    --label-black: #000000;
    --burst-light: #e6e6e6;
    --burst-mid: #bcbcbc;
    --ink: #1a1a1a;
    --figure-tone: #2b2b2b;
  }
  html, body {
    margin: 0;
    padding: 0;
    overflow: hidden;
    background: var(--page);
  }
  .canvas {
    position: relative;
    width: 1200px;
    height: 792px;
    overflow: hidden;
    background: var(--page);
  }
  .label {
    position: absolute;
    left: 87px;
    top: 44px;
    width: 1047px;
    height: 693px;
    background: var(--label-black);
    overflow: hidden;
  }
  .burst {
    position: absolute;
    inset: 0;
    background: radial-gradient(ellipse 50% 50% at 50% 50%,
      var(--burst-light) 0%,
      var(--burst-light) 64%,
      var(--burst-mid) 84%,
      var(--label-black) 100%);
  }
  .portrait {
    position: absolute;
    left: 232px;
    top: 196px;
    width: 160px;
    height: 360px;
    background: linear-gradient(180deg, var(--figure-tone) 0%, #4a4a4a 100%);
    border-radius: 80px 80px 20px 20px;
  }
  .brand-name {
    position: absolute;
    left: 418px;
    top: 272px;
    margin: 0;
    font-family: "Oleo Script", "Georgia", serif;
    font-weight: 700;
    font-size: 120px;
    line-height: 1;
    color: var(--ink);
    transform: rotate(-6deg);
    transform-origin: left center;
    letter-spacing: 1px;
    white-space: nowrap;
  }
  .wine-type {
    position: absolute;
    left: 100px;
    top: 476px;
    margin: 0;
    font-family: "Arimo", "Arial", sans-serif;
    font-size: 44px;
    line-height: 1;
    color: var(--ink);
    white-space: nowrap;
  }
</style>
</head>
<body>
  <main class="canvas">
    <section class="label">
      <div class="burst" role="img" aria-label="Light starburst of radiating rays on black"></div>
      <div class="portrait" role="img" aria-label="Black line illustration of a woman holding a glass"></div>
      <h1 class="brand-name">Corvinte</h1>
      <p class="wine-type">White</p>
    </section>
  </main>
</body>
</html>
```